Tarnholt Bright Press Label

We are looking for a label for our blueberry vodka and lemonade ready-to-drink cocktail. we would like the ingredients (vodka, lemon juice, cane sugar, blueberries) discretely displayed on the label. We would also like 15% alc/vol (30 proof) on the label. The label is for a 12-ounce slim can. We would also like the Surgeon Generals warning ion the label

Target Market(s)

Spike seltzer and ready to drink cocktail drinkers

Font styles to use
Decorative

Requirements
Must have
• Surgeon General warning, 15% alc/vol (30 proof) 12 ounces., Ingredients

```html
<!DOCTYPE html>
<html lang="en">
<head>
<meta charset="utf-8">
<title>Tarnholt Bright Press – Lemonade Cocktail Label</title>
<link rel="stylesheet" href="https://fonts.googleapis.com/css2?family=Amiri&family=Londrina+Solid:wght@900&family=Barlow+Semi+Condensed:wght@800&family=Barlow+Condensed:wght@500&display=swap">
<style>
  :root {
    --page-bg: #ececec;
    --label-top: #fdd44e;
    --label-bottom: #fdbd2c;
    --arch-fill: #fee07a;
    --arch-line: #f7a823;
    --band: #f9a51b;
    --lemon-art: #fbd95a;
    --ink: #2a2415;
    --white: #ffffff;
  }
  * { margin: 0; padding: 0; box-sizing: border-box; }
  html, body {
    width: 1200px;
    height: 1200px;
    overflow: hidden;
    background: var(--page-bg);
  }
  .label {
    position: absolute;
    left: 383px;
    top: 50px;
    width: 434px;
    height: 1100px;
    display: block;
  }
  .tagline { font-family: 'Amiri', serif; font-size: 40px; fill: var(--ink); letter-spacing: 1px; }
  .product-name { font-family: 'Londrina Solid', cursive; font-weight: 900; font-size: 112px; fill: var(--white); stroke: var(--ink); stroke-width: 2; paint-order: stroke; letter-spacing: 2px; }
  .product-type { font-family: 'Barlow Semi Condensed', sans-serif; font-weight: 800; font-size: 158px; fill: var(--white); }
  .ingredients { font-family: 'Amiri', serif; font-size: 38px; fill: var(--ink); }
  .strength { font-family: 'Barlow Condensed', sans-serif; font-weight: 500; font-size: 19px; fill: var(--ink); }
  .warning { font-family: 'Barlow Condensed', sans-serif; font-weight: 500; font-size: 12.5px; fill: var(--ink); }
  .volume { font-family: 'Amiri', serif; font-size: 34px; fill: var(--ink); }
</style>
</head>
<body>
<svg class="label" viewBox="0 0 697 1768" xmlns="http://www.w3.org/2000/svg">
  <defs>
    <path id="tagline-arc" d="M 100 180 Q 348 -10 600 180"/>
  </defs>

  <rect class="label-top" x="0" y="0" width="697" height="1262" fill="var(--label-top)"/>
  <rect class="label-bottom" x="0" y="1262" width="697" height="506" fill="var(--label-bottom)"/>

  <text class="tagline" text-anchor="middle">
    <textPath href="#tagline-arc" startOffset="50%">READY-TO-DRINK COCKTAIL</textPath>
  </text>

  <path class="arch" d="M 70 712 L 70 440 A 278 278 0 0 1 626 440 L 626 712 Z"
        fill="var(--arch-fill)" stroke="var(--arch-line)" stroke-width="4"/>

  <ellipse class="lemon-art" cx="330" cy="400" rx="215" ry="195" fill="var(--lemon-art)"
           role="img" aria-label="Illustration of a lemon with green leaves"/>

  <rect class="name-band" x="0" y="712" width="697" height="148" fill="var(--band)"/>
  <text class="product-name" x="348" y="832" text-anchor="middle">LEMONADE</text>

  <text class="product-type" x="340" y="1012" text-anchor="middle">COCKTAIL</text>

  <text class="ingredients" text-anchor="middle">
    <tspan x="348" y="1095">Vodka, Lemon Juice, Cane Sugar,</tspan>
    <tspan x="348" y="1135">Blueberries</tspan>
  </text>

  <text class="strength" text-anchor="middle">
    <tspan x="108" y="1193">30</tspan>
    <tspan x="108" y="1220">PROOF</tspan>
  </text>
  <text class="strength" text-anchor="middle">
    <tspan x="580" y="1193">15%</tspan>
    <tspan x="580" y="1220">ALC/VOL</tspan>
  </text>

  <text class="warning" transform="translate(44 1640) rotate(-90)">
    <tspan x="0" y="0">WARNING: Smoking Causes Lung Cancer, Heart Disease, Emphysema,</tspan>
    <tspan x="0" y="16">and May Complicate Pregnancy.</tspan>
  </text>

  <text class="volume" text-anchor="middle">
    <tspan x="348" y="1572">12 fl oz</tspan>
    <tspan x="348" y="1608">(355 ml)</tspan>
  </text>
</svg>
</body>
</html>
```